Home page design for a live auction website.

Hi, we are looking at finding a good design for an auction website, only home page .. We will not be selling anything online, so the website will only be a portal where visitors can check about our company, upcoming auctions, online catalogues etc.
See attached our logo. Please use the same red that you see on the logo in the designs that you provide.
The final design should communicate high-end auction website, as we will be selling expensive piece of arts and antiques.
We should have a main frame where images of arts will circulate, with description of the art piece. just like on http://paris.vellmarotte-quisande.com/
(but with a better design overall) and of course a menu with different tabs, like "about us", "previous sales" "next sales", "contact" , "how to buy", "meet our specialists".

Target Market(s)

High end segment, who can afford to pay up to 250'000 for a piece of art

Industry/Entity Type

Online

Number of Pages Required

1 page

Requirements
Must have
• a frame with images rotating, just like on http://paris.vellmarotte-quisande.com/ . but the rest of the design should be more refined.
• we should also have a strong call to action, "Free online estimation", click here, estimation delivered in 48 hours"
Nice to have
• Tremaux Auctions, the brand should be well visible

```html
<!DOCTYPE html>
<html lang="en">
<head>
<meta charset="utf-8">
<title>Tremaux Auctions – Home</title>
<link href="https://fonts.googleapis.com/css2?family=Open+Sans:wght@300;400;600;700&display=swap" rel="stylesheet">
<style>
:root{
  --red:#c4232b;
  --red-dark:#a51a21;
  --ink:#333;
  --muted:#8a8a8a;
  --line:#e2e2e2;
  --band:#f1f1f1;
  --dark:#2c2c2c;
  --paper:#fff;
}
*{box-sizing:border-box;margin:0;padding:0}
html,body{width:758px;height:1200px;overflow:hidden}
body{position:relative;background:var(--paper);font-family:'Open Sans',Arial,sans-serif;color:var(--ink);font-size:7px;line-height:1.45}
.abs{position:absolute}
.top-rule{left:0;top:0;width:758px;height:3px;background:var(--red)}
/* header */
.brand{left:55px;top:14px;display:flex;align-items:center;gap:6px}
.brand-mark{width:14px;height:14px;background:var(--red)}
.brand-name{font-size:13px;font-weight:600;color:var(--red);letter-spacing:.3px}
.main-nav{right:50px;top:20px;display:flex;gap:28px}
.main-nav a{font-size:7px;font-weight:600;color:#777;text-decoration:none;letter-spacing:.4px;text-transform:uppercase;padding-bottom:10px}
.main-nav a.active{color:var(--red);border-bottom:2px solid var(--red)}
.header-rule{left:0;top:55px;width:758px;height:1px;background:var(--line)}
/* hero */
.slider{left:55px;top:70px;width:438px;height:246px}
.slide-art{width:100%;height:200px;background:linear-gradient(120deg,#6b4b3a 0%,#b8434a 30%,#e5b049 52%,#3a78a8 72%,#5c3b60 100%)}
.slide-caption{height:46px;background:var(--paper);border:1px solid var(--line);border-top:0;padding:9px 14px}
.slide-caption p{font-size:8px;color:#555}
.slide-caption a{font-size:6.5px;color:var(--red);text-decoration:none;font-weight:600}
.slide-dots{position:absolute;right:12px;bottom:16px;display:flex;gap:4px}
.slide-dots i{width:5px;height:5px;border-radius:50%;background:#ccc}
.slide-dots i.on{background:var(--red)}
.cta-estimate{left:505px;top:70px;width:203px;height:140px;background:var(--dark);color:#fff;text-align:center;padding-top:14px}
.cta-estimate h2{font-size:17px;font-weight:600;line-height:1.15;letter-spacing:.5px}
.cta-estimate .btn{display:inline-block;margin-top:12px;background:var(--red);color:#fff;font-size:8px;font-weight:700;padding:6px 22px;text-transform:uppercase}
.cta-estimate .note{margin-top:12px;font-size:6.5px;color:#ddd}
.cta-catalogue{left:505px;top:210px;width:203px;height:63px;background:var(--band);text-align:center;padding-top:10px;border:1px solid var(--line)}
.cta-catalogue h3{font-size:12px;font-weight:600;color:#444;text-transform:uppercase;letter-spacing:.5px}
.cta-catalogue .btn{display:inline-block;margin-top:6px;background:var(--red);color:#fff;font-size:7px;font-weight:700;padding:4px 18px;text-transform:uppercase}
.cta-phone{left:505px;top:280px;width:203px;display:flex;align-items:center;gap:8px}
.cta-phone small{display:block;font-size:6px;color:var(--muted)}
.cta-phone strong{font-size:11px;font-weight:600;color:var(--red)}
/* headings */
.section-title{font-size:13px;font-weight:400;color:#444;text-transform:uppercase;letter-spacing:.6px}
.section-title.red{color:var(--red);text-transform:none;font-size:12px}
/* about */
.about-title{left:55px;top:340px}
.about-photo{left:55px;top:380px;width:100px;height:100px;background:linear-gradient(160deg,#7a5a3e,#3d2d22);border:3px solid #eee}
.about-text{left:215px;top:382px;width:493px;color:#777;font-size:6.5px}
.about-text p+p{margin-top:6px}
.about-band{left:0;top:520px;width:758px;height:28px;background:var(--band)}
/* upcoming */
.upcoming-title{left:55px;top:571px}
.upcoming-rule{left:55px;top:592px;width:438px;height:1px;background:var(--line)}
.lot{width:215px;height:80px;display:flex;gap:9px}
.lot-art{width:76px;height:68px;flex:none}
.lot-date{color:var(--red);font-size:6px;font-weight:600}
.lot-name{font-size:7.5px;font-weight:700;color:#333}
.lot-desc{font-size:6px;color:var(--muted);line-height:1.35}
.lot-actions{margin-top:5px;display:flex;align-items:center;gap:6px;font-size:6px;color:var(--muted)}
.lot-actions span.btn{background:#cfcfcf;color:#fff;padding:2px 10px;font-weight:600}
/* sales sidebar */
.sales{left:530px;top:571px;width:178px;height:300px;border:1px solid var(--line)}
.sales-tabs{display:flex}
.sales-tabs span{flex:1;text-align:center;font-size:6.5px;font-weight:600;padding:6px 0;text-transform:uppercase;color:var(--muted);background:var(--band)}
.sales-tabs span.on{background:var(--red);color:#fff}
.sale{display:flex;gap:7px;padding:9px 8px;border-bottom:1px solid var(--line)}
.sale:last-child{border-bottom:0}
.sale-art{width:58px;height:58px;flex:none}
/* specialists */
.specialists-band{left:0;top:883px;width:758px;height:135px;background:var(--band)}
.specialists-title{left:0;top:892px;width:758px;text-align:center}
.specialist{width:180px;display:flex;gap:10px;align-items:center}
.avatar{width:52px;height:52px;border-radius:50%;flex:none;background:linear-gradient(#c9c9c9,#9a9a9a)}
.specialist b{display:block;font-size:7.5px;color:#333}
.specialist span{font-size:6px;color:var(--muted)}
.arrow{top:956px}
/* footer */
.site-footer{left:0;top:1018px;width:758px;height:146px;background:var(--red);color:#fff}
.footer-notch{left:369px;top:1012px}
.footer-col{top:1036px;width:140px;font-size:6px;line-height:1.6;color:#f6d7d8}
.footer-col h4{font-size:7px;color:#fff;font-weight:700;margin-bottom:3px}
.footer-bar{left:0;top:1164px;width:758px;height:36px;background:var(--paper)}
.footer-brand{left:55px;top:1175px;display:flex;align-items:center;gap:5px}
.footer-brand .brand-mark{width:10px;height:10px}
.footer-brand .brand-name{font-size:9px}
.footer-copy{left:175px;top:1179px;font-size:6px;color:var(--muted)}
.footer-mail{left:330px;top:1178px;font-size:6.5px;color:var(--muted);display:flex;gap:5px;align-items:center}
.footer-call{right:50px;top:1174px;display:flex;gap:6px;align-items:center}
.footer-call small{font-size:6px;color:var(--muted)}
.footer-call strong{font-size:10px;color:var(--red);font-weight:600}
</style>
</head>
<body>
<div class="abs top-rule"></div>

<header>
  <div class="abs brand"><span class="brand-mark"></span><span class="brand-name">Tremaux Auctions</span></div>
  <nav class="abs main-nav">
    <a class="active">Home</a><a>Previous Sales</a><a>Next Sales</a><a>How to Buy</a><a>Meet our Specialists</a><a>Contact</a>
  </nav>
  <div class="abs header-rule"></div>
</header>

<section class="abs slider">
  <div class="slide-art" role="img" aria-label="Featured artwork: colourful street mural along a narrow lane"></div>
  <div class="slide-caption">
    <p>Maecenas a enim eget lorem consectetur</p>
    <a>READ MORE</a>
  </div>
  <div class="slide-dots"><i class="on"></i><i></i><i></i><i></i></div>
</section>

<aside class="abs cta-estimate">
  <h2>FREE ONLINE<br>ESTIMATION</h2>
  <span class="btn">Click here ›</span>
  <p class="note">Estimation delivered in 48 hours</p>
</aside>
<aside class="abs cta-catalogue">
  <h3>Online Catalogues</h3>
  <span class="btn">Download ›</span>
</aside>
<div class="abs cta-phone">
  <svg width="18" height="18" viewBox="0 0 24 24"><circle cx="12" cy="12" r="12" fill="#c4232b"/><path d="M8.5 6.5l2 2-1.2 1.6c.8 1.6 2 2.8 3.6 3.6l1.6-1.2 2 2-1.4 1.8c-3.8-.6-7.2-4-7.8-7.8z" fill="#fff"/></svg>
  <div><small>For more information</small><strong>Call us on: 1800 555 014</strong></div>
</div>

<h2 class="abs section-title about-title">About our company</h2>
<div class="abs about-photo" role="img" aria-label="Auction house interior with framed paintings"></div>
<div class="abs about-text">
  <p>Nulla consequat orci torquent fringilla pretium. Suspendisse accumsan leo eu consectetur feugiat. Sed interdum cursus risus, nec aliquam tellus volutpat id. Cras nec lectus lacus, in vehicula nunc fringilla in augue. In vitae dui et nibh convallis pretium. Aliquam vehicula varius tellus. Quisque in feugiat tellus. Sed feugiat lacinia mi sollicitudin. Donec iaculis quam.</p>
  <p>Maecenas in lorem eget posuere consequat. Vestibulum in nisi ut odio blandit varius. Ut sollicitudin, est vitae scelerisque, elementum nibh at dolor dolor. Donec non lectus sollicitudin, porta quam vel, malesuada nulla fermentum. Proin hendrerit aliquam lacus id dolor tristique. Aliquam integer metus purus ipsum. Nulla ac placerat quam. Nullam sit amet lorem aliquet.</p>
</div>
<div class="abs about-band"></div>

<h2 class="abs section-title upcoming-title">Upcoming auctions</h2>
<div class="abs upcoming-rule"></div>

<article class="abs lot" style="left:55px;top:602px"><div class="lot-art" role="img" aria-label="Antique pocket watch" style="background:linear-gradient(135deg,#8c7a5c,#3e3426)"></div><div><div class="lot-date">26 janvier 2013 11:00</div><div class="lot-name">Nulla consequat</div><div class="lot-desc">Maecenas a enim eget lorem consectetur fermentum sed nunc.</div><div class="lot-actions"><span class="btn">VIEW</span>Catalogue</div></div></article>
<article class="abs lot" style="left:278px;top:602px"><div class="lot-art" role="img" aria-label="Vintage brass clock" style="background:linear-gradient(135deg,#c9a46a,#5b4631)"></div><div><div class="lot-date">26 janvier 2013 11:00</div><div class="lot-name">Nulla consequat</div><div class="lot-desc">Maecenas a enim eget lorem consectetur fermentum sed nunc.</div><div class="lot-actions"><span class="btn">VIEW</span>Catalogue</div></div></article>
<article class="abs lot" style="left:55px;top:688px"><div class="lot-art" role="img" aria-label="Colourful abstract painting" style="background:linear-gradient(135deg,#e0a23b,#b13c35,#3d6e9a)"></div><div><div class="lot-date">26 janvier 2013 11:00</div><div class="lot-name">Nulla consequat</div><div class="lot-desc">Maecenas a enim eget lorem consectetur fermentum sed nunc.</div><div class="lot-actions"><span class="btn">VIEW</span>Catalogue</div></div></article>
<article class="abs lot" style="left:278px;top:688px"><div class="lot-art" role="img" aria-label="Painted artwork in warm tones" style="background:linear-gradient(135deg,#d9622f,#7c2a2a)"></div><div><div class="lot-date">26 janvier 2013 11:00</div><div class="lot-name">Nulla consequat</div><div class="lot-desc">Maecenas a enim eget lorem consectetur fermentum sed nunc.</div><div class="lot-actions"><span class="btn">VIEW</span>Catalogue</div></div></article>
<article class="abs lot" style="left:55px;top:774px"><div class="lot-art" role="img" aria-label="Bright modern canvas" style="background:linear-gradient(135deg,#e6c23a,#6aa34a,#2f6e8f)"></div><div><div class="lot-date">26 janvier 2013 11:00</div><div class="lot-name">Nulla consequat</div><div class="lot-desc">Maecenas a enim eget lorem consectetur fermentum sed nunc.</div><div class="lot-actions"><span class="btn">VIEW</span>Catalogue</div></div></article>
<article class="abs lot" style="left:278px;top:774px"><div class="lot-art" role="img" aria-label="Abstract painting in red and teal" style="background:linear-gradient(135deg,#2f8a8a,#c33b4a,#e7a24a)"></div><div><div class="lot-date">26 janvier 2013 11:00</div><div class="lot-name">Nulla consequat</div><div class="lot-desc">Maecenas a enim eget lorem consectetur fermentum sed nunc.</div><div class="lot-actions"><span class="btn">VIEW</span>Catalogue</div></div></article>

<aside class="abs sales">
  <div class="sales-tabs"><span class="on">Previous sales</span><span>Next sales</span></div>
  <div class="sale"><div class="sale-art" role="img" aria-label="Sold artwork in blue tones" style="background:linear-gradient(135deg,#5c86a8,#26384a)"></div><div><div class="lot-date">26 janvier 2013 11:00</div><div class="lot-name">Nulla consequat</div><div class="lot-desc">Maecenas a enim eget lorem consectetur.</div></div></div>
  <div class="sale"><div class="sale-art" role="img" aria-label="Sold landscape painting" style="background:linear-gradient(135deg,#9bb36a,#3f5a34)"></div><div><div class="lot-date">26 janvier 2013 11:00</div><div class="lot-name">Nulla consequat</div><div class="lot-desc">Maecenas a enim eget lorem consectetur.</div></div></div>
  <div class="sale"><div class="sale-art" role="img" aria-label="Sold colourful canvas" style="background:linear-gradient(135deg,#e57b3a,#c0304a,#5d3a8a)"></div><div><div class="lot-date">26 janvier 2013 11:00</div><div class="lot-name">Nulla consequat</div><div class="lot-desc">Maecenas a enim eget lorem consectetur.</div></div></div>
</aside>

<div class="abs specialists-band"></div>
<h2 class="abs section-title red specialists-title">Meet our specialist</h2>
<svg class="abs arrow" style="left:20px" width="10" height="14" viewBox="0 0 10 14"><path d="M8 1L2 7l6 6" stroke="#999" stroke-width="2" fill="none"/></svg>
<svg class="abs arrow" style="left:728px" width="10" height="14" viewBox="0 0 10 14"><path d="M2 1l6 6-6 6" stroke="#999" stroke-width="2" fill="none"/></svg>
<div class="abs specialist" style="left:75px;top:935px"><div class="avatar" role="img" aria-label="Portrait of a specialist"></div><div><b>Henri Valcourt</b><span>Maecenas a enim eget lorem consectetur fermentum</span></div></div>
<div class="abs specialist" style="left:290px;top:935px"><div class="avatar" role="img" aria-label="Portrait of a specialist"></div><div><b>Henri Valcourt</b><span>Maecenas a enim eget lorem consectetur fermentum</span></div></div>
<div class="abs specialist" style="left:505px;top:935px"><div class="avatar" role="img" aria-label="Portrait of a specialist"></div><div><b>Henri Valcourt</b><span>Maecenas a enim eget lorem consectetur fermentum</span></div></div>

<footer>
  <div class="abs site-footer"></div>
  <svg class="abs footer-notch" width="20" height="8" viewBox="0 0 20 8"><path d="M0 8L10 0l10 8z" fill="#c4232b"/></svg>
  <div class="abs footer-col" style="left:55px"><h4>About us</h4>Company history<br>Our team<br>Our experts<br>Press<br>Careers<br>Contact us</div>
  <div class="abs footer-col" style="left:215px"><h4>How to buy</h4>Registration<br>Bidding online<br>Payment terms<br>Shipping options<br>Buyer fees<br>Conditions of sale</div>
  <div class="abs footer-col" style="left:375px"><h4>Sales</h4>Previous sales results<br>Upcoming sales list<br>Online catalogues<br>Private sales desk<br>Free estimation<br>Sale calendar</div>
  <div class="abs footer-col" style="left:540px"><h4>Place of auction</h4>Main saleroom<br>Viewing hours daily<br>Opening times<br>Access and parking<br>Contact the desk<br>Press enquiries</div>
  <div class="abs footer-bar"></div>
  <div class="abs footer-brand"><span class="brand-mark"></span><span class="brand-name">Tremaux Auctions</span></div>
  <div class="abs footer-copy">Copyright © 2013</div>
  <div class="abs footer-mail"><svg width="10" height="7" viewBox="0 0 10 7"><rect x=".5" y=".5" width="9" height="6" fill="none" stroke="#999"/><path d="M.5.5L5 4 9.5.5" fill="none" stroke="#999"/></svg>info@tremauxauctions.com</div>
  <div class="abs footer-call"><svg width="14" height="14" viewBox="0 0 24 24"><circle cx="12" cy="12" r="12" fill="#c4232b"/><path d="M8.5 6.5l2 2-1.2 1.6c.8 1.6 2 2.8 3.6 3.6l1.6-1.2 2 2-1.4 1.8c-3.8-.6-7.2-4-7.8-7.8z" fill="#fff"/></svg><div><small>For more information</small><br><strong>Call us on: 1800 555 014</strong></div></div>
</footer>
</body>
</html>
```